Brightmere Pictures Business Card

Hello,

i would like to have a dynamic, creative but tasteful card, colour used, front and back. I have attached a sample card that I liked very much from another individual to give you an idea of the theme/approach, but not colour. Ideally the graphic elements of the Brightmere Logo are brought into the design.

Target Market(s)

North America

Industry/Entity Type

Film Production

Contact Information for Business Card

Nadia Pellwick
President/Founder
Brightmere Pictures Inc.
403 555 2917
nadia@brightmerepictures.tv

Font styles to use
Sans Serif

Colors
6b449b
5c5c5c
fdfdfd
000000

Requirements
Must have
• Logo, name, Company name, email and cell number. no Address line to be included.
Should not have
• any unrelated GFX elements, serif fonts

```html
<!DOCTYPE html>
<html lang="en">
<head>
<meta charset="utf-8">
<title>Brightmere Pictures Business Card</title>
<link href="https://fonts.googleapis.com/css2?family=Bebas+Neue&family=Questrial&display=swap" rel="stylesheet">
<style>
  :root {
    --purple: #6b449b;
    --grey: #5c5c5c;
    --charcoal: #3f3f41;
    --paper: #fdfdfd;
    --ink: #000000;
    --stage: #1c1c1c;
  }
  * { margin: 0; padding: 0; box-sizing: border-box; }
  html, body {
    width: 1200px;
    height: 1000px;
    overflow: hidden;
    background: var(--stage);
  }
  .stage {
    width: 1200px;
    height: 1000px;
    display: flex;
    align-items: center;
    justify-content: center;
    gap: 40px;
  }
  .card {
    position: relative;
    width: 525px;
    height: 300px;
    background: var(--paper);
    border-radius: 18px;
    overflow: hidden;
  }
  /* Front */
  .card-front {
    display: flex;
    align-items: center;
    justify-content: center;
    gap: 14px;
  }
  .brand-dot {
    width: 30px;
    height: 30px;
    border-radius: 50%;
    background: var(--purple);
  }
  .brand-name {
    font-family: "Questrial", sans-serif;
    font-size: 52px;
    color: var(--grey);
    letter-spacing: -1px;
  }
  /* Back */
  .back-shapes {
    position: absolute;
    inset: 0;
  }
  .shape-charcoal { fill: var(--charcoal); }
  .shape-purple { fill: var(--purple); }
  .bunting {
    position: absolute;
    left: 220px;
    top: 128px;
    width: 215px;
    height: 16px;
    background: linear-gradient(90deg, var(--charcoal), var(--purple), var(--charcoal), var(--purple), var(--charcoal));
  }
  .holder {
    position: absolute;
    right: 95px;
    top: 62px;
    text-align: right;
  }
  .holder-name {
    font-family: "Bebas Neue", sans-serif;
    font-size: 38px;
    line-height: 1;
    color: var(--purple);
    letter-spacing: 1px;
  }
  .holder-title {
    font-family: "Questrial", sans-serif;
    font-size: 15px;
    color: var(--ink);
  }
  .contact {
    position: absolute;
    left: 145px;
    top: 160px;
  }
  .contact-company {
    font-family: "Bebas Neue", sans-serif;
    font-size: 28px;
    line-height: 1;
    color: var(--purple);
    letter-spacing: 0.5px;
  }
  .contact-line {
    font-family: "Questrial", sans-serif;
    font-size: 17px;
    line-height: 1.25;
    color: var(--ink);
  }
</style>
</head>
<body>
<main class="stage">
  <section class="card card-front" aria-label="Card front">
    <span class="brand-dot"></span>
    <span class="brand-name">brightmere</span>
  </section>

  <section class="card card-back" aria-label="Card back">
    <svg class="back-shapes" viewBox="0 0 525 300" width="525" height="300" aria-hidden="true">
      <polygon class="shape-charcoal" points="0,0 80,0 55,300 0,300"/>
      <polygon class="shape-purple" points="95,0 232,0 105,120"/>
      <polygon class="shape-purple" points="340,300 440,300 440,170"/>
      <polygon class="shape-charcoal" points="452,0 525,0 525,300 472,300"/>
    </svg>
    <div class="bunting" role="img" aria-label="Bunting of alternating charcoal and purple pennants"></div>
    <div class="holder">
      <p class="holder-name">Nadia Pellwick</p>
      <p class="holder-title">President/Founder</p>
    </div>
    <div class="contact">
      <p class="contact-company">Brightmere Pictures Inc.</p>
      <p class="contact-line">403 555 2917</p>
      <p class="contact-line">nadia@brightmerepictures.tv</p>
    </div>
  </section>
</main>
</body>
</html>
```